Billboard advertisement design

Health & Fitness centre requires a billboard advertisement design for an allocated space out the front of the shopping centre in which it is located. Kestrel Ridge Health & Fitness is located in a small town with one other competitor. Looking for a fun, trendy sign to draw people's attention and make sure Kestrel Ridge is instantly recognisable. Sign location is in the middle of town on the national highway. Approximate size is 12' x 5'. Final design will encourage people who have been thinking about joining the gym to take the first step in leading a fitter and healthier lifestyle.

Target Market(s)

Health conscious members of the community that have been thinking about taking the next step and joining a gym

Industry/Entity Type

Shopping

Requirements
Must have
• Please utilise attached logo
Nice to have
• Contact info is (07) 4918 5307 info@kestrelridgefitness.example.com.au

```html
<!DOCTYPE html>
<html lang="en">
<head>
<meta charset="utf-8">
<title>Kestrel Ridge Health &amp; Fitness — Billboard</title>
<link rel="stylesheet" href="https://fonts.googleapis.com/css2?family=Bebas+Neue&family=Oswald:wght@400;700&display=swap">
<style>
  :root {
    --page-bg: #e8ebef;
    --wall-dark: #4d4c45;
    --wall-mid: #6e6d63;
    --wall-light: #8a887c;
    --ink-white: #ffffff;
    --brand-blue: #1f5fa8;
    --photo-skin: #b07a55;
    --photo-shadow: #5b4636;
  }
  * { margin: 0; padding: 0; box-sizing: border-box; }
  html, body {
    width: 1200px; height: 801px; overflow: hidden;
    background: var(--page-bg);
  }
  .billboard {
    position: absolute; left: 50px; top: 171px;
    width: 1100px; height: 459px; overflow: hidden;
    background:
      radial-gradient(ellipse 40% 50% at 30% 30%, rgba(255,255,255,0.08), transparent 70%),
      radial-gradient(ellipse 35% 45% at 75% 60%, rgba(0,0,0,0.12), transparent 70%),
      linear-gradient(135deg, var(--wall-mid), var(--wall-dark) 55%, var(--wall-light));
  }
  .hero-photo {
    position: absolute; left: 40px; top: 40px;
    width: 540px; height: 419px;
    background: radial-gradient(ellipse 55% 70% at 50% 55%, var(--photo-skin), var(--photo-shadow) 75%, transparent 100%);
  }
  .headline {
    position: absolute; left: 565px; top: 118px; width: 510px;
    font-family: "Bebas Neue", "Oswald", sans-serif;
    color: var(--ink-white);
    font-size: 84px; line-height: 0.92; letter-spacing: 2px;
    text-align: right;
  }
  .headline span { display: block; }
  .headline .line-two { padding-right: 70px; }
  .contact-email {
    position: absolute; left: 40px; top: 335px;
    font-family: "Oswald", sans-serif; font-weight: 400;
    font-size: 13px; letter-spacing: 3.5px;
    color: var(--ink-white); text-transform: uppercase;
  }
  .brand-band { position: absolute; left: 0; top: 0; width: 1100px; height: 459px; }
  .brand-name {
    position: absolute; right: 55px; top: 375px;
    font-family: "Oswald", sans-serif; font-weight: 700;
    font-size: 44px; letter-spacing: 1px;
    color: var(--brand-blue); text-transform: uppercase;
  }
</style>
</head>
<body>
  <section class="billboard">
    <div class="hero-photo" role="img" aria-label="Photo of a fit man and woman lifting dumbbells"></div>
    <h1 class="headline">
      <span class="line-one">Make a change!</span>
      <span class="line-two">Join now!</span>
    </h1>
    <p class="contact-email">info@kestrelridgefitness.example.com.au</p>
    <svg class="brand-band" viewBox="0 0 1100 459" aria-hidden="true">
      <path d="M610 459 C 680 380, 760 340, 880 330 L 1100 330 L 1100 459 Z" fill="#ffffff"/>
    </svg>
    <div class="brand-name">Kestrel Ridge</div>
  </section>
</body>
</html>
```